Golden Thimble Embroidery & Gifts

Embroidery & Promotional Items. We would like the brochure to be bright and colorful. Have each panel portraying different aspects of our business. We really are clueless on the best way to design something like this. We really encourage you to use your own creativity. Please let me know any questions you may have for us. Thank you

how do I close and accept

Target Market(s)

Individuals and Families as well as corporate clients

Font styles to use
Sans Serif
Script

Colors
33a6d7
b868aa

Requirements
Must have
• Embroidery, Promotional. Corporate, Commemorative Gifts, Vinyl lettering, About us, are headlines of each section if possible

```html
<!DOCTYPE html>
<html lang="en">
<head>
<meta charset="utf-8">
<title>Golden Thimble Embroidery & Gifts – Brochure</title>
<link href="https://fonts.googleapis.com/css2?family=Comic+Neue:wght@400;700&family=Lobster+Two:wght@700&family=Great+Vibes&family=Montserrat:wght@400;500&display=swap" rel="stylesheet">
<style>
:root{
  --blue:#33a6d7;
  --blue-deep:#2a97c9;
  --blue-light:#6cc2e6;
  --pink:#c2185b;
  --thread:#b03a5b;
  --paper:#f1f1f1;
  --paper-shade:#dedede;
  --ink:#1d1d1d;
  --white:#ffffff;
  --stage:#e8e5e1;
}
*{box-sizing:border-box;margin:0;padding:0}
html,body{width:826px;height:1200px;overflow:hidden;background:var(--stage)}
.sheet{position:absolute;left:43px;width:740px;height:572px;overflow:hidden;background:var(--paper);box-shadow:0 2px 8px rgba(0,0,0,.25)}
.sheet--outside{top:18px}
.sheet--inside{top:610px}
.panel{position:absolute;overflow:hidden}
.paper{background:linear-gradient(90deg,var(--paper) 0%,#fafafa 60%,var(--paper-shade) 100%)}
.section{position:absolute;left:0;right:0;padding:0 14px 0 16px;overflow:hidden}
.kicker{font-family:"Montserrat",sans-serif;font-size:9.5px;color:var(--pink);margin-top:10px}
.headline{font-family:"Lobster Two",cursive;font-size:24px;color:var(--blue);line-height:28px}
.rule{height:2px;background:var(--thread);margin:4px -14px 0 -16px}
.copy{font-family:"Comic Neue",sans-serif;font-size:10px;line-height:12.3px;color:var(--ink);margin-top:12px}
.photo{position:absolute}
.band{position:absolute;background:var(--blue);color:var(--white)}
.contact{text-align:center;font-family:"Montserrat",sans-serif;font-size:11px;line-height:14px;padding-top:30px}
.contact .phone-label{margin-top:12px;display:block}
.contact .phone{font-size:18px;line-height:22px}
.slogan{font-family:"Great Vibes",cursive;font-size:38px;line-height:42px;text-align:center;padding-top:20px}
.brand{position:absolute;display:flex;align-items:center;gap:10px;left:26px;top:72px}
.brand-dot{width:36px;height:36px;border-radius:50%;background:var(--thread);flex:none}
.brand-name{font-family:"Comic Neue",sans-serif;font-weight:700;font-size:19px;line-height:22px;color:var(--blue-deep)}
.what{background:linear-gradient(90deg,var(--blue-light),var(--blue) 70%,var(--blue-deep))}
.what-box{position:absolute;left:20px;top:56px;width:210px;height:500px;background:rgba(255,255,255,.18)}
.what-tag{position:absolute;left:45px;top:40px;width:164px;height:33px;background:var(--pink);border-radius:4px;color:var(--white);font-family:"Montserrat",sans-serif;font-size:11px;line-height:33px;text-align:center}
.what-title{position:absolute;left:20px;width:210px;top:80px;text-align:center;font-family:"Lobster Two",cursive;font-size:24px;color:var(--white)}
.what-copy{position:absolute;left:32px;width:190px;top:114px;font-family:"Montserrat",sans-serif;font-size:9.4px;line-height:12.2px;color:var(--white)}
.what-copy p{margin-bottom:12px}
.owners{display:flex;gap:12px;margin-top:12px;align-items:flex-start}
.owners-photo{width:70px;height:72px;border-radius:4px;background:linear-gradient(135deg,#8a8f96,#3b3f45);flex:none;box-shadow:0 1px 3px rgba(0,0,0,.4)}
.owners .copy{margin-top:0}
</style>
</head>
<body>

<section class="sheet sheet--outside">
  <div class="panel paper" style="left:0;top:0;width:247px;height:572px">
    <article class="section" style="top:0;height:268px">
      <p class="kicker">A Little Something about</p>
      <h2 class="headline">Baby</h2>
      <div class="rule"></div>
      <p class="copy">Golden Thimble Embroidery &amp; Gifts was founded by Rita and Tom Marlowe in 2003. Prior to starting our business we both worked in corporate America - Rita was a department head for a large national company and Tom was supervisor at a customer service call center. We were both caught up in a layoff within a month of each other. We started with a small home embroidery sewing machine and sold items online as well as personalized clothes for our children and extended family members. As our business has grown, we have added more equipment and currently have five commercial machines that allow us to</p>
    </article>
    <article class="section" style="top:268px;height:304px">
      <p class="kicker">A Little Something about</p>
      <h2 class="headline">Vinyl lettering</h2>
      <div class="rule"></div>
      <p class="copy">Golden Thimble Embroidery &amp; Gifts was founded by Rita and Tom Marlowe in 2003. Prior to starting our business we both worked in corporate America - Rita was a department head for a large national company and Tom was supervisor at a customer service call center. We were both caught up in a layoff within a month of each other. We started with a small home embroidery sewing machine and sold items online as well as personalized clothes for our children and extended family members. As our business has grown, we have added more equipment and currently have five commercial machines that allow us to provide long-lasting, professional products.</p>
    </article>
  </div>

  <div class="photo" role="img" aria-label="Three people wearing embroidered polo, blouse and robe" style="left:247px;top:0;width:247px;height:227px;background:linear-gradient(180deg,#ececec,#d9d9d9)"></div>

  <div class="panel paper" style="left:494px;top:0;width:246px;height:227px">
    <div class="brand">
      <span class="brand-dot"></span>
      <span class="brand-name">Golden Thimble<br>Embroidery &amp; Gifts</span>
    </div>
  </div>

  <div class="band contact" style="left:247px;top:227px;width:247px;height:139px">
    <p>4120-B W. Harlan Ave<br>Maple Falls, OK 74000</p>
    <span class="phone-label">Phone:</span>
    <p class="phone">(555) 014-2290</p>
  </div>
  <div class="band slogan" style="left:494px;top:227px;width:246px;height:139px;background:linear-gradient(90deg,var(--blue-deep),var(--blue))">
    <p>Logo Wear.<br>Gifts. Apparel.</p>
  </div>

  <div class="photo" role="img" aria-label="Brick storefront of the embroidery and gifts shop" style="left:247px;top:366px;width:493px;height:206px;background:linear-gradient(180deg,#8a6a56 0%,#7a5a48 55%,#3f4a55 80%,#5a5a5a 100%)"></div>
</section>

<section class="sheet sheet--inside">
  <div class="panel what" style="left:0;top:0;width:249px;height:572px">
    <div class="what-box"></div>
    <div class="what-tag">A Little Something about</div>
    <h2 class="what-title">What We Do</h2>
    <div class="what-copy">
      <p>We offer custom embroidery for all your corporate and personalized gift needs.</p>
      <p>Golden Thimble is a full-service custom embroidery business. We are very flexible and work closely with our customers to make sure that your order is "just right".</p>
      <p>We offer a complete range of corporate products including apparel, hats, briefcases, tote bags, golf towels, and promotional products.</p>
      <p>Our quality personalized gift products are second to none. We offer gifts for every occasion - baby, birthdays, graduation, weddings, anniversaries, Mother's Day, Father's Day, and holidays. Towels, towel sets, sports towels, fleece blankets, woven cotton throws, robes, shower and spa wraps, baby blankets, pillows, and pillowcases are just a few of the items we offer.</p>
      <p>In addition to embroidered products, we offer a unique selection of heat-transfer sublimated products which include coffee cups, mouse pads, coasters, puzzles, jewelry boxes, license plates, serving trays, desk accessories, t-shirts, and ornaments.</p>
    </div>
  </div>

  <div class="panel paper" style="left:249px;top:0;width:247px;height:572px">
    <article class="section" style="top:16px;height:380px">
      <p class="kicker">A Little Something about</p>
      <h2 class="headline">Tom &amp; Rita</h2>
      <div class="rule"></div>
      <p class="copy">Golden Thimble Embroidery &amp; Gifts was founded by Rita and Tom Marlowe in 2003. Prior to starting our business we both worked in corporate America - Rita was a department head for a large national company and Tom was supervisor at a customer service call center. We were both caught up in a layoff within a month of each other. We started with a small home embroidery sewing machine and sold items online as well as personalized clothes for our children and extended family members. As our business has grown, we have added more equipment and currently have five commercial machines that allow us to provide long-lasting, professional products.</p>
      <div class="owners">
        <div class="owners-photo" role="img" aria-label="Portrait of the two owners"></div>
        <p class="copy">We are currently located in the Westgate Plaza Shopping Center on the North-East corner of 12th &amp; Harlan.</p>
      </div>
    </article>
    <article class="section" style="top:396px;height:176px">
      <h2 class="headline" style="margin-top:14px">Embroidery</h2>
      <div class="rule"></div>
      <p class="copy" style="margin-top:16px">Golden Thimble Embroidery &amp; Gifts was founded by Rita and Tom Marlowe in 2003. Prior to starting our business we both worked in corporate America - Rita was a department head for a large national company and Tom was supervisor at a customer service call center. We were both caught up in a layoff within a month of each other. We started</p>
    </article>
  </div>

  <div class="panel paper" style="left:496px;top:0;width:244px;height:572px">
    <article class="section" style="top:16px;height:262px">
      <p class="kicker">A Little Something about</p>
      <h2 class="headline">Promotional</h2>
      <div class="rule"></div>
      <p class="copy">Golden Thimble Embroidery &amp; Gifts was founded by Rita and Tom Marlowe in 2003. Prior to starting our business we both worked in corporate America - Rita was a department head for a large national company and Tom was supervisor at a customer service call center. We were both caught up in a layoff within a month of each other. We started with a small home embroidery sewing machine and sold items online as well as personalized clothes for our children and extended family members. As our business has grown, we have added more equipment and currently have five commercial machines that allow us to</p>
    </article>
    <article class="section" style="top:278px;height:294px">
      <p class="kicker">A Little Something about</p>
      <h2 class="headline">Corporate</h2>
      <div class="rule"></div>
      <p class="copy">Golden Thimble Embroidery &amp; Gifts was founded by Rita and Tom Marlowe in 2003. Prior to starting our business we both worked in corporate America - Rita was a department head for a large national company and Tom was supervisor at a customer service call center. We were both caught up in a layoff within a month of each other. We started with a small home embroidery sewing machine and sold items online as well as personalized clothes for our children and extended family members. As our business has grown, we have added more equipment and currently have five commercial machines that allow us to provide long-lasting, professional products.</p>
    </article>
  </div>
</section>

</body>
</html>
```